Regenerative Medicine Brochure

I want a clean modern bi-fold or tri-fold brochure. We offer non-surgical joint repair for knees, shoulders, and hips. We have many services available including regenerative medicine including stem cell allograft, palatelet rich plasma, prolotherapy, triggerpoint injection, chiropractic and rehab therapies. We are a modern multidisciplinary clinic in coastal California. My logo is already complete and is a vibrant green color. I prefer lots of white space with some areas for service description and what conditions may benefit from the services. Design should convey modern treatments, upscale office and practice, and our target audience is older adults who want to maintain an active pain-free lifestyle.

Target Market(s)

Sports injuries, athletes, seniors who are active, knee pain, shoulder pain, arthritis.

Industry/Entity Type

Alternative Medicine

Font styles to use
Serif

Colors
9bcb3c

Requirements
Must have
• Small white space where we can write date, time, location of next event/class. Colors in brochure to coordinate with logo colors provided.

```html
<!DOCTYPE html>
<html lang="en">
<head>
<meta charset="utf-8">
<title>Regenerative Medicine Treatment – Coastline Joint Care</title>
<link rel="stylesheet" href="https://fonts.googleapis.com/css2?family=Libre+Baskerville:wght@400;700&display=swap">
<style>
  :root {
    --green: #4cb748;
    --white: #ffffff;
    --ink: #1a1a1a;
    --panel-grey: #eeeeee;
    --star: #f6c62b;
  }
  * { margin: 0; padding: 0; box-sizing: border-box; }
  html, body { width: 1200px; height: 848px; overflow: hidden; background: var(--white); }
  body { font-family: "Libre Baskerville", Georgia, serif; color: var(--ink); }
  .brochure { position: relative; width: 1200px; height: 848px; }

  /* Left panel */
  .panel-left { position: absolute; left: 0; top: 0; width: 398px; height: 848px; background: var(--white); }
  .photo { position: absolute; width: 177px; height: 127px; }
  .photo--shoulder { left: 17px; top: 13px; background: linear-gradient(160deg, #6c8f4e, #b9c7a4 55%, #e9e2d8); }
  .photo--elbow { left: 204px; top: 13px; background: linear-gradient(150deg, #2f4f8f, #c98f6c 60%, #dfe6ea); }
  .photo--wrist { left: 17px; top: 150px; background: linear-gradient(140deg, #e3b48a, #d9cbb6 55%, #efe9e1); }
  .photo--back { left: 205px; top: 150px; background: linear-gradient(170deg, #c9ccd0, #e8e8e8 45%, #8ba35c 80%, #a0533f); }
  .photo--knee { left: 17px; top: 288px; background: linear-gradient(160deg, #1d6a78, #5f7fa6 55%, #2a7c86); }
  .photo--ankle { left: 205px; top: 288px; background: linear-gradient(150deg, #eae6e1, #e4a9b4 45%, #3c5b8c 75%, #ece8e2); }

  .reviews { position: absolute; left: 16px; top: 430px; width: 363px; height: 396px; background: var(--panel-grey); padding: 18px 19px 0 19px; }
  .review__name { font-weight: 700; font-size: 17px; letter-spacing: 0.3px; display: flex; align-items: center; gap: 5px; }
  .stars { display: flex; gap: 2px; }
  .stars svg { width: 18px; height: 18px; fill: var(--star); }
  .review__text { font-size: 15.6px; line-height: 20.6px; text-align: justify; margin-top: 10px; }
  .review + .review { margin-top: 19px; }

  /* Middle panel */
  .panel-contact { position: absolute; left: 398px; top: 0; width: 404px; height: 848px; background: var(--green); color: var(--white); text-align: center; }
  .icon-badge { position: absolute; left: 180px; width: 43px; height: 43px; border-radius: 50%; background: var(--white); display: flex; align-items: center; justify-content: center; }
  .icon-badge svg { width: 22px; height: 22px; fill: none; stroke: var(--green); stroke-width: 1.8; stroke-linecap: round; stroke-linejoin: round; }
  .contact-heading { position: absolute; left: 0; width: 100%; font-weight: 700; font-size: 17.5px; letter-spacing: 0.5px; }
  .contact-line { position: absolute; left: 0; width: 100%; font-size: 15px; letter-spacing: 0.8px; }

  /* Right panel */
  .panel-cover { position: absolute; left: 802px; top: 0; width: 398px; height: 848px; }
  .panel-cover svg.cover-shapes { position: absolute; inset: 0; }
  .cover-title { position: absolute; left: 0; top: 538px; width: 398px; text-align: center; color: var(--white); font-weight: 700; font-size: 30px; line-height: 34px; letter-spacing: 1.2px; }
  .brand { position: absolute; left: 0; top: 748px; width: 398px; display: flex; align-items: center; justify-content: center; gap: 12px; }
  .brand__dot { width: 16px; height: 16px; border-radius: 50%; background: var(--green); }
  .brand__name { font-size: 27px; font-weight: 400; color: var(--ink); }
</style>
</head>
<body>
<main class="brochure">

  <section class="panel-left">
    <div class="photo photo--shoulder" role="img" aria-label="Photo of a woman holding her sore shoulder outdoors"></div>
    <div class="photo photo--elbow" role="img" aria-label="Photo of a man holding his painful elbow"></div>
    <div class="photo photo--wrist" role="img" aria-label="Photo of a woman holding her aching wrist"></div>
    <div class="photo photo--back" role="img" aria-label="Photo of a man holding his lower back on a running track"></div>
    <div class="photo photo--knee" role="img" aria-label="Photo of a man holding his knee while standing up from a sofa"></div>
    <div class="photo photo--ankle" role="img" aria-label="Photo of a woman holding her sore ankle"></div>

    <div class="reviews">
      <article class="review">
        <h3 class="review__name">MARISOL T.
          <span class="stars">
            <svg viewBox="0 0 24 24"><path d="M12 1l3.4 7.1 7.6.9-5.6 5.3 1.5 7.7L12 18.2 5.1 22l1.5-7.7L1 9l7.6-.9z"/></svg>
            <svg viewBox="0 0 24 24"><path d="M12 1l3.4 7.1 7.6.9-5.6 5.3 1.5 7.7L12 18.2 5.1 22l1.5-7.7L1 9l7.6-.9z"/></svg>
            <svg viewBox="0 0 24 24"><path d="M12 1l3.4 7.1 7.6.9-5.6 5.3 1.5 7.7L12 18.2 5.1 22l1.5-7.7L1 9l7.6-.9z"/></svg>
            <svg viewBox="0 0 24 24"><path d="M12 1l3.4 7.1 7.6.9-5.6 5.3 1.5 7.7L12 18.2 5.1 22l1.5-7.7L1 9l7.6-.9z"/></svg>
            <svg viewBox="0 0 24 24"><path d="M12 1l3.4 7.1 7.6.9-5.6 5.3 1.5 7.7L12 18.2 5.1 22l1.5-7.7L1 9l7.6-.9z"/></svg>
          </span>
        </h3>
        <p class="review__text">“ I have been a patient with Dr. Halden for 9 years and I have Always been pleased with my treatments. Dr. Halden and his staff are so kind hearted and I highly recommend all of my family and friends to go to his practice! ”</p>
      </article>
      <article class="review">
        <h3 class="review__name">DANA R.
          <span class="stars">
            <svg viewBox="0 0 24 24"><path d="M12 1l3.4 7.1 7.6.9-5.6 5.3 1.5 7.7L12 18.2 5.1 22l1.5-7.7L1 9l7.6-.9z"/></svg>
            <svg viewBox="0 0 24 24"><path d="M12 1l3.4 7.1 7.6.9-5.6 5.3 1.5 7.7L12 18.2 5.1 22l1.5-7.7L1 9l7.6-.9z"/></svg>
            <svg viewBox="0 0 24 24"><path d="M12 1l3.4 7.1 7.6.9-5.6 5.3 1.5 7.7L12 18.2 5.1 22l1.5-7.7L1 9l7.6-.9z"/></svg>
            <svg viewBox="0 0 24 24"><path d="M12 1l3.4 7.1 7.6.9-5.6 5.3 1.5 7.7L12 18.2 5.1 22l1.5-7.7L1 9l7.6-.9z"/></svg>
            <svg viewBox="0 0 24 24"><path d="M12 1l3.4 7.1 7.6.9-5.6 5.3 1.5 7.7L12 18.2 5.1 22l1.5-7.7L1 9l7.6-.9z"/></svg>
          </span>
        </h3>
        <p class="review__text">“ I've been going to Dr.Halden for a couple of years now and I wouldn't go to anyone else! I'm very picky when it comes to my health care, so to find him and his amazing staff I can only say that there's no better! They are the best in the business! Thank you Dr. Halden and to your amazing staff! ”</p>
      </article>
    </div>
  </section>

  <section class="panel-contact">
    <div class="icon-badge" style="top:100px">
      <svg viewBox="0 0 24 24"><path d="M6.5 3.5l3 3.2-1.8 2.1a11 11 0 0 0 7.5 7.5l2.1-1.8 3.2 3-2 2.5C11 19.5 4.5 13 4 5.5z"/></svg>
    </div>
    <h2 class="contact-heading" style="top:181px">CONTACT&nbsp; US</h2>
    <p class="contact-line" style="top:227px">For Appointments : 805-555-0142</p>
    <p class="contact-line" style="top:255px">For General Inquiries : 805-555-0187</p>

    <div class="icon-badge" style="top:344px">
      <svg viewBox="0 0 24 24"><rect x="3" y="5.5" width="18" height="13" rx="1"/><path d="M3 6l9 7 9-7M3 18l7-6.5M21 18l-7-6.5"/></svg>
    </div>
    <h2 class="contact-heading" style="top:425px">WRITE TO US</h2>
    <p class="contact-line" style="top:471px">hello@coastlinejointcare.com</p>

    <div class="icon-badge" style="top:563px">
      <svg viewBox="0 0 24 24"><path d="M12 22s-7-7.5-7-12.5a7 7 0 0 1 14 0C19 14.5 12 22 12 22z"/><circle cx="12" cy="9.5" r="2.6"/></svg>
    </div>
    <h2 class="contact-heading" style="top:644px">VISIT US</h2>
    <p class="contact-line" style="top:690px">420 Harbor View Rd</p>
    <p class="contact-line" style="top:719px">Pismo Grove, CA 93499</p>
  </section>

  <section class="panel-cover">
    <svg class="cover-shapes" viewBox="0 0 398 848" width="398" height="848">
      <defs>
        <linearGradient id="knee-photo" x1="0" y1="0" x2="1" y2="1">
          <stop offset="0" stop-color="#e9e6e3"/>
          <stop offset="0.35" stop-color="#d9a48a"/>
          <stop offset="0.55" stop-color="#f08a58"/>
          <stop offset="0.8" stop-color="#4e5661"/>
          <stop offset="1" stop-color="#3d4450"/>
        </linearGradient>
      </defs>
      <polygon points="0,0 398,0 398,503 0,463" fill="url(#knee-photo)" role="img" aria-label="Photo of a person holding a knee with a glowing joint overlay"/>
      <polygon points="0,463 398,503 398,635 0,715" fill="var(--green)"/>
    </svg>
    <h1 class="cover-title">Regenerative<br>Medicine Treatment</h1>
    <div class="brand">
      <span class="brand__dot"></span>
      <span class="brand__name">Coastline Joint Care</span>
    </div>
  </section>

</main>
</body>
</html>
```